Up to the Challenge? Canadian based consulting company needs a two sided business card design

A Canadian based security risk management consulting company needs a two-sided business card design. What we do is provide advice and guidance related to emergency, security and business continuity management for small, medium and large companies to help ensure the protection of their people, assets, information, services, operations and reputation.

The final design should be simple, only one or two colours, eye catching, professional and one that makes people look at three or more times just because it looks so darn good.

I have include examples of business cards I like.

Target Market(s)

Small, medium and large companies.

Industry/Entity Type

Security

Contact Information for Business Card

Business Card Size: Standard size of 3.5" (89mm) x 2.0" (51mm) - (see full specifications and guides on PRINTLY's website if required)
Card Stock: Looking to use PRINTLY's Velm 32pt stock textured paper - seam colour either chili red or black
Business Name: The Harrowgate Partners
Website: www.theharrowgatepartners.example
Telephone: (555)310-2968
Name: Dana Ostrander
Position: Principle
e-mail: Dana.Ostrander@theharrowgatepartners.example

Font styles to use
Serif

Colors
ec1f27
000000
9d9d9d
aaaaaa
606060

Requirements
Must have
• - "The Harrowgate Partners" logo (see uploaded files). I have included grey scale and colour versions.
• - Business card details (as above)
Nice to have
• - One side black or grey scale.
• - Other side would likely be white.
• - Everyone likes the silver logo on the black background.
• - Small element of colour i.e. red but I'm leaning more to greyscale.
Should not have
• - A lot of colour. Keep it simple.

```html
<!DOCTYPE html>
<html lang="en">
<head>
<meta charset="utf-8">
<title>The Harrowgate Partners — Business Card</title>
<link href="https://fonts.googleapis.com/css2?family=Cinzel:wght@400;600&display=swap" rel="stylesheet">
<style>
  :root {
    --brand-red: #ec1f27;
    --ink-black: #000000;
    --silver: #9d9d9d;
    --silver-light: #aaaaaa;
    --graphite: #606060;
    --paper: #ffffff;
    --text-dark: #2b2b2b;
    --backdrop: #e6e6e6;
  }
  * { box-sizing: border-box; margin: 0; padding: 0; }
  html, body { width: 1200px; height: 898px; overflow: hidden; }
  body {
    background: var(--backdrop);
    font-family: "Cinzel", "Times New Roman", serif;
    position: relative;
  }
  .card {
    position: absolute;
    top: 299px;
    width: 525px;
    height: 300px;
    box-shadow: 0 6px 18px rgba(0,0,0,0.18);
    overflow: hidden;
  }

  /* Company name with plain square marker */
  .company {
    display: flex;
    align-items: center;
    font-weight: 400;
    white-space: nowrap;
  }
  .company-mark { flex: none; }

  /* Front side */
  .card-front {
    left: 50px;
    background: var(--ink-black);
    display: flex;
    align-items: center;
    justify-content: center;
  }
  .card-front .company {
    color: var(--silver);
    font-size: 24px;
    gap: 18px;
  }
  .card-front .company-mark {
    width: 44px;
    height: 44px;
    background: var(--silver);
  }

  /* Back side */
  .card-back {
    left: 625px;
    background: var(--paper);
  }
  .card-back .company {
    position: absolute;
    left: 30px;
    top: 34px;
    color: var(--graphite);
    font-size: 13px;
    gap: 10px;
  }
  .card-back .company-mark {
    width: 18px;
    height: 18px;
    background: var(--graphite);
  }
  .person {
    position: absolute;
    left: 250px;
    top: 82px;
    padding-left: 12px;
    border-left: 2px solid var(--brand-red);
  }
  .person-name {
    font-size: 22px;
    font-weight: 600;
    letter-spacing: 1.5px;
    color: var(--text-dark);
  }
  .person-role {
    font-size: 10px;
    font-weight: 600;
    letter-spacing: 1.5px;
    color: var(--brand-red);
    margin-top: 2px;
  }
  .contact-list {
    position: absolute;
    left: 210px;
    top: 170px;
    list-style: none;
  }
  .contact-item {
    display: flex;
    align-items: center;
    gap: 8px;
    color: var(--text-dark);
    font-size: 7.5px;
    letter-spacing: 0.3px;
    margin-bottom: 9px;
  }
  .contact-item.phone { font-size: 17px; letter-spacing: 1px; margin-bottom: 11px; }
  .contact-icon { width: 11px; height: 11px; flex: none; }
  .edge-rule {
    position: absolute;
    left: 0; right: 0;
  }
  .edge-rule.grey { bottom: 12px; height: 1px; background: var(--silver-light); }
  .edge-rule.red { bottom: 6px; height: 3px; background: var(--brand-red); }
</style>
</head>
<body>

  <section class="card card-front" aria-label="Card front">
    <h1 class="company">The Harrowgate Partners<span class="company-mark" aria-hidden="true"></span></h1>
  </section>

  <section class="card card-back" aria-label="Card back">
    <p class="company">The Harrowgate Partners<span class="company-mark" aria-hidden="true"></span></p>

    <div class="person">
      <h2 class="person-name">DANA OSTRANDER</h2>
      <p class="person-role">PRINCIPLE</p>
    </div>

    <ul class="contact-list">
      <li class="contact-item phone">
        <svg class="contact-icon" viewBox="0 0 24 24" aria-hidden="true">
          <path fill="#ec1f27" d="M6.6 10.8a15.1 15.1 0 0 0 6.6 6.6l2.2-2.2a1 1 0 0 1 1-.25 11.4 11.4 0 0 0 3.6.57 1 1 0 0 1 1 1V20a1 1 0 0 1-1 1A17 17 0 0 1 3 4a1 1 0 0 1 1-1h3.5a1 1 0 0 1 1 1 11.4 11.4 0 0 0 .57 3.6 1 1 0 0 1-.25 1z"/>
        </svg>
        (555)310-2968
      </li>
      <li class="contact-item email">
        <svg class="contact-icon" viewBox="0 0 24 24" aria-hidden="true">
          <rect x="2" y="5" width="20" height="14" rx="1.5" fill="#ec1f27"/>
          <path d="M3 6l9 7 9-7" fill="none" stroke="#ffffff" stroke-width="1.6"/>
        </svg>
        DANA.OSTRANDER@THEHARROWGATEPARTNERS.EXAMPLE
      </li>
      <li class="contact-item web">
        <svg class="contact-icon" viewBox="0 0 24 24" aria-hidden="true">
          <circle cx="12" cy="12" r="10" fill="#ec1f27"/>
          <path d="M2 12h20M12 2c3 3 3 17 0 20M12 2c-3 3-3 17 0 20" fill="none" stroke="#ffffff" stroke-width="1.3"/>
        </svg>
        WWW.THEHARROWGATEPARTNERS.EXAMPLE
      </li>
    </ul>

    <div class="edge-rule grey"></div>
    <div class="edge-rule red"></div>
  </section>

</body>
</html>
```